Now Leasing Banner

Looking for a banner that says the following information approx 4' x 30'

Now Leasing Maplewood Terrace 925-318-6054

Target Market(s)

Drive by traffic

Industry/Entity Type

Residential property management

Requirements
Must have
• Clear and readable from a distance

```html
<!DOCTYPE html>
<html lang="en">
<head>
<meta charset="utf-8">
<title>Now Leasing Banners – Maplewood Terrace</title>
<link rel="stylesheet" href="https://fonts.googleapis.com/css2?family=Bebas+Neue&display=swap">
<style>
  :root {
    --charcoal: #363636;
    --red: #ed1c24;
    --yellow: #fff200;
    --white: #ffffff;
    --bg-light: #f2f2f2;
    --bg-dark: #7e7e7e;
  }
  html, body {
    margin: 0;
    padding: 0;
    width: 1200px;
    height: 675px;
    overflow: hidden;
  }
  .canvas {
    position: relative;
    width: 1200px;
    height: 675px;
    background: radial-gradient(ellipse 55% 65% at 40% 50%, var(--bg-light) 0%, #c4c4c4 55%, var(--bg-dark) 100%);
    font-family: "Bebas Neue", "Oswald", sans-serif;
  }
  .banner {
    position: absolute;
    left: 134px;
    width: 931px;
    height: 124px;
    overflow: hidden;
    box-shadow: 0 10px 14px -6px rgba(0, 0, 0, 0.35);
  }
  .banner--white { top: 84px; }
  .banner--red { top: 276px; }
  .banner--yellow { top: 473px; }
  .banner__shape {
    position: absolute;
    inset: 0;
    display: block;
  }
  .banner__text {
    position: absolute;
    margin: 0;
    line-height: 1;
    white-space: nowrap;
  }
  .headline {
    left: 17px;
    top: 6px;
    font-size: 139px;
    color: var(--white);
    letter-spacing: 1px;
  }
  .contact-name {
    left: 634px;
    top: 15px;
    font-size: 44px;
    letter-spacing: -0.5px;
    color: var(--red);
  }
  .contact-phone {
    left: 632px;
    top: 60px;
    font-size: 63px;
    color: var(--charcoal);
  }
  .lockup-now {
    left: 26px;
    top: 22px;
    font-size: 107px;
    color: var(--white);
  }
  .lockup-leasing {
    left: 191px;
    top: 17px;
    font-size: 64px;
    color: var(--yellow);
  }
  .lockup-name {
    left: 192px;
    top: 82px;
    font-size: 25px;
    color: var(--white);
  }
  .big-phone {
    left: 395px;
    top: 15px;
    font-size: 113px;
    color: var(--white);
    letter-spacing: 1px;
  }
  .big-phone--dark {
    color: var(--charcoal);
    text-shadow:
      2px 2px 0 var(--yellow),
      4px 4px 0 var(--charcoal),
      5px 5px 0 var(--charcoal),
      6px 6px 0 var(--charcoal);
  }
</style>
</head>
<body>
<main class="canvas">

  <section class="banner banner--white" aria-label="Now Leasing banner, white contact panel">
    <svg class="banner__shape" width="931" height="124" viewBox="0 0 931 124" aria-hidden="true">
      <rect width="931" height="124" fill="var(--white)"/>
      <polygon points="0,0 592,0 620,62 592,124 0,124" fill="var(--charcoal)"/>
    </svg>
    <h1 class="banner__text headline">Now Leasing</h1>
    <p class="banner__text contact-name">Maplewood Terrace</p>
    <p class="banner__text contact-phone">925-318-6054</p>
  </section>

  <section class="banner banner--red" aria-label="Now Leasing banner, red phone panel">
    <svg class="banner__shape" width="931" height="124" viewBox="0 0 931 124" aria-hidden="true">
      <rect width="931" height="124" fill="var(--red)"/>
      <polygon points="0,0 358,0 380,62 358,124 0,124" fill="var(--charcoal)"/>
    </svg>
    <p class="banner__text lockup-now">Now</p>
    <p class="banner__text lockup-leasing">Leasing</p>
    <p class="banner__text lockup-name">Maplewood Terrace</p>
    <p class="banner__text big-phone">925-318-6054</p>
  </section>

  <section class="banner banner--yellow" aria-label="Now Leasing banner, yellow phone panel">
    <svg class="banner__shape" width="931" height="124" viewBox="0 0 931 124" aria-hidden="true">
      <rect width="931" height="124" fill="var(--yellow)"/>
      <polygon points="12,0 358,0 380,62 358,124 12,124" fill="var(--charcoal)"/>
    </svg>
    <p class="banner__text lockup-now">Now</p>
    <p class="banner__text lockup-leasing">Leasing</p>
    <p class="banner__text lockup-name">Maplewood Terrace</p>
    <p class="banner__text big-phone big-phone--dark">925-318-6054</p>
  </section>

</main>
</body>
</html>
```